Design for online reviews widget

Attached is a wireframe of a widget we need designing to display reviews on websites from multiple sources. We need this provided at 3 different sizes including full screen, contained (like the wireframe) and mobile.
You have completely free rein on the styling.
The only elements that should remain untouched are the blue stars (https://www.filevault-demo.net/s/8pwtmz2lq4nv90h/kt%20stars.ai?dl=0) and powered by logo at the bottom.
Ignore the menu at the top of the wireframe, this is just from the website the widget will be placed on.
Target Market(s)
Businesses
Look and feel
Each slider illustrates characteristics of the customer's brand and the style your logo design should communicate.

```html
<!DOCTYPE html>
<html lang="en">
<head>
<meta charset="utf-8">
<title>Reviews Widget</title>
<link href="https://fonts.googleapis.com/css2?family=Poppins:wght@300;400;500;600&family=Roboto+Condensed:wght@400&display=swap" rel="stylesheet">
<style>
:root{
  --nav-bg:#2a2a2a;
  --nav-active:#5a9e2f;
  --panel:#efeeee;
  --card:#ffffff;
  --card-muted:#f8f8f8;
  --ink:#111111;
  --body:#555555;
  --muted:#8a8a8a;
  --sky:#3dbde8;
  --sky-soft:#92d9f2;
  --green:#5a9e2f;
  --btn:#349a42;
  --navy:#0e5aa7;
  --star-soft:#8fd2ee;
  --star-mint:#7fd6a4;
}
*{margin:0;padding:0;box-sizing:border-box}
html,body{width:972px;height:1200px;overflow:hidden;background:#fff;font-family:"Poppins",sans-serif}
.site-nav{position:absolute;top:4px;left:0;width:972px;height:38px;background:var(--nav-bg);display:flex;justify-content:center;align-items:stretch;font-family:"Roboto Condensed",sans-serif;font-size:10px;color:#fff}
.site-nav span{display:flex;align-items:center;padding:0 11px}
.site-nav .active{background:var(--nav-active)}
.widget{position:absolute;left:105px;top:63px;width:764px;height:1137px;background:var(--panel);border-radius:8px 8px 0 0}
.summary{position:absolute;left:0;top:25px;width:100%;text-align:center;font-size:11.5px;color:var(--ink)}
.summary svg{display:block;margin:0 auto 6px}
.filter{position:absolute;right:14px;top:34px;width:164px;height:31px;border:1px solid #d6d6d6;border-radius:16px;background:#fff;font-size:8.5px;color:#999;display:flex;align-items:center;justify-content:space-between;padding:0 14px}
.card{position:absolute;left:16px;width:734px;border-radius:8px;background:var(--card-muted);padding:0 40px 0 50px}
.card.featured{background:var(--card);box-shadow:0 8px 16px rgba(0,0,0,.16)}
.card-head{display:flex;justify-content:space-between;align-items:center;height:42px;margin-top:18px}
.card-title{font-size:16px;font-weight:500;color:var(--muted)}
.featured .card-title{color:var(--ink)}
.source{display:flex;align-items:center;gap:22px}
.source-name{font-size:13px;font-weight:500;color:#777}
.featured .source-name{color:#d8201e}
.score{width:38px;height:38px;border-radius:50%;background:var(--navy);border:2px solid #fff;box-shadow:0 0 0 2px var(--navy);color:#fff;font-size:9.5px;font-weight:500;display:flex;align-items:center;justify-content:center}
.card-body{margin-top:16px;font-size:9.6px;line-height:17.2px;color:var(--muted);font-weight:300}
.featured .card-body{color:var(--body)}
.card-body b{font-weight:500;color:#333}
.featured .card-body .metrics{color:var(--ink);font-weight:400}
.tags{display:flex;gap:8px;margin-top:18px;margin-left:-2px}
.tag{height:16px;padding:0 9px;border-radius:8px;font-size:9.5px;color:#fff;display:flex;align-items:center}
.tag.sky{background:var(--sky)}
.tag.soft{background:var(--sky-soft);font-weight:300}
.tag.green{background:var(--green)}
.load-more{position:absolute;left:281px;top:970px;width:204px;height:51px;border-radius:26px;background:var(--btn);color:#fff;font-size:15px;font-weight:600;display:flex;align-items:center;justify-content:center}
.powered{position:absolute;left:574px;top:1068px;width:150px;text-align:right;font-size:11px;color:#222}
.powered .brand{display:flex;align-items:center;justify-content:flex-end;gap:6px;margin-top:4px;font-size:17px;font-weight:600;color:#222}
.powered .mark{width:14px;height:14px;background:var(--sky);border-radius:50%}
</style>
</head>
<body>
<nav class="site-nav">
  <span>HOME</span><span>ABOUT ▼</span><span>WINDOWS ▼</span><span>DOORS ▼</span><span>ORANGERIES &amp; EXTENSIONS ▼</span><span>ROOFS ▼</span><span>OUR WORK ▼</span><span class="active">REVIEWS ▼</span><span>BLOG</span><span>CONTACT</span>
</nav>

<main class="widget">
  <div class="summary">
    <svg width="154" height="28" viewBox="0 0 154 28" aria-label="Five stars">
      <defs>
        <g id="rating-star">
          <circle cx="14" cy="14" r="14" fill="var(--sky)"/>
          <path d="M14 5.5l2.5 5.3 5.8.7-4.3 4 1.1 5.7L14 18.4l-5.1 2.8 1.1-5.7-4.3-4 5.8-.7z" fill="#fff"/>
        </g>
      </defs>
      <use href="#rating-star" x="0"/><use href="#rating-star" x="32"/><use href="#rating-star" x="64"/><use href="#rating-star" x="96"/><use href="#rating-star" x="126"/>
    </svg>
    Combined Review Score 4.3 out of 5
  </div>
  <div class="filter">Filter Results <span>⌄</span></div>

  <article class="card featured" style="top:102px;height:200px">
    <div class="card-head">
      <h2 class="card-title">Front door with windows each side and side window</h2>
      <div class="source"><span class="source-name">TradeVouch</span><span class="score">9.77</span></div>
    </div>
    <p class="card-body">This is the second time we have used Crestmoor Home Improvements , and the service is amazing! Marcus came round several times as we keep changing our minds and he was so helpful and gave us good advice, and the guys who do the fitting are efficient and tidy . I've got to say the end result is amazing and I have recommended to many of friends . Thanks Crestmoor<br><span class="metrics"><b>Reliablity:</b> 9.38 <b>Courtesy:</b> 10 <b>Tidiness:</b> 9.84 <b>Workmanship:</b> 10</span></p>
    <div class="tags"><span class="tag sky">Verified 28th September 2021</span><span class="tag green">Located in Ashford</span></div>
  </article>

  <article class="card" style="top:313px;height:195px">
    <div class="card-head">
      <h2 class="card-title">Positive: Professionalism, Quality, Value</h2>
      <div class="source"><svg width="86" height="14" viewBox="0 0 86 14" aria-label="Five stars"><g fill="var(--star-soft)"><path id="small-star" d="M7 0l2.1 4.5 4.9.6-3.6 3.4.9 4.9L7 11l-4.3 2.4.9-4.9L0 5.1l4.9-.6z"/><use href="#small-star" x="18"/><use href="#small-star" x="36"/><use href="#small-star" x="54"/><use href="#small-star" x="72"/></g></svg><span class="source-name">Searchly</span></div>
    </div>
    <p class="card-body">The team did a good job of replacing a large feature window spanning two floors, as well as the others in my property. They're a professional group who were willing to work out solutions to any problem, especially compared to other companies. Prices are fair, and my new UPVC windows look great. Special thanks to Owen for being so accommodating and for the good communication throughout.<br><b>Service:</b> <span style="color:#444">Window installation</span></p>
    <div class="tags"><span class="tag soft">11 months ago by Daniel Porter</span></div>
  </article>

  <article class="card" style="top:522px;height:199px">
    <div class="card-head">
      <h2 class="card-title">Brilliant all round professional, friendly service.</h2>
      <div class="source"><svg width="86" height="14" viewBox="0 0 86 14" aria-label="Five stars"><g fill="var(--star-soft)"><use href="#small-star"/><use href="#small-star" x="18"/><use href="#small-star" x="36"/><use href="#small-star" x="54"/><use href="#small-star" x="72"/></g></svg><span class="source-name">Listbook</span></div>
    </div>
    <p class="card-body">This home run friendly business was a real pleasure to deal with. From the professional, no pressure quote, nothing was too much trouble to ensure everything is as required for your needs with the quote and fitting. The workmanship and double glazing being fitted was brilliant and my home/outdoors was left tidy and clean leaving an outstanding impression for such an all round professional job. I would not hesitate to recommend this company, such a brilliant service from great hardworking people that care about their service.</p>
    <div class="tags"><span class="tag soft">13 Feb 2018 by GreenLamp42</span></div>
  </article>

  <article class="card" style="top:737px;height:188px">
    <div class="card-head">
      <h2 class="card-title">Front door with windows each side and side window</h2>
      <div class="source"><svg width="86" height="14" viewBox="0 0 86 14" aria-label="Five stars"><g fill="var(--star-mint)"><use href="#small-star"/><use href="#small-star" x="18"/><use href="#small-star" x="36"/><use href="#small-star" x="54"/><use href="#small-star" x="72"/></g></svg><span class="source-name">TrustLane</span></div>
    </div>
    <p class="card-body">This is the second time we have used Crestmoor Home Improvements , and the service is amazing! Marcus came round several times as we keep changing our minds and he was so helpful and gave us good advice, and the guys who do the fitting are<br>efficient and tidy . I've got to say the end result is amazing and I have recommended to many of friends . Thanks Crestmoor</p>
    <div class="tags"><span class="tag soft">13 Feb 2018 by Jo</span></div>
  </article>

  <div class="load-more">LOAD MORE</div>

  <div class="powered">Powered by<div class="brand"><span class="mark"></span>ReviewMerge</div></div>
</main>
</body>
</html>
```